Tovo's Grist - Flour Bag Packing for Fit and Healthy Flour

Tovo's Grist is a family owned company that was incorporated in honor of our grandfather who is in the pic below. We would like to incorporate that picture into the packaging design. We would also like for the logo to represent a modern/fit lifestyle that is unique from the current competition.

Tovo's flour is a newly practiced style of milling that allows for flour to be consumed in its natural/organic state. We don't not bleach, chemically treat or add any enriched/preservative additives to our flour. This allows for freshness (our priority) and the natural flavors of the nutty grain to seep into our flour.

Our flour contains all the nutritional value that comes from all the components of Wheat Family Grains.

Our Family has been in the flour business for 60+ years and we established our mill in Debar Macedonia in 1998.

100% Organic
Non GMO
Family Owned
Stone Milled
Banner (Product Types): All Purpose Flour, Whole Wheat Flour, Pastry Flour, Artisan (Bread) Flour
Size: 1 KG / 5 KG / 25 KG

Flour is good for: Cookies, Cakes, Bread, Biscuits, Brownies, Muffins, Pastries, Pancakes, Rolls, Pizza Crust Pies

Target Market(s)

Fit Lifestyle, Hipsters, Modern, NYC

Industry/Entity Type

Agtech

Logo Text

Tovo's Grist

Requirements
Must have
• Tovo's Pic must be incorporated somehow on the bag. He will provide a friendly face and a homier feeling. The pic does not need to be the Center Piece. The logo will be the Center Piece.
Nice to have
• Tovo's Grist on the side of the bags or some cool/hip design.

```html
<!DOCTYPE html>
<html lang="en">
<head>
<meta charset="utf-8">
<title>Tovo's Flour – Bag Panels</title>
<link rel="stylesheet" href="https://fonts.googleapis.com/css2?family=Oswald:wght@500;700&family=Ubuntu:wght@500;700&family=PT+Sans+Narrow:wght@400;700&display=swap">
<style>
  :root {
    --brown: #7a4a14;
    --gold: #b08a1e;
    --gold-light: #cfa53c;
    --green: #5a8a2a;
    --paper: #fbfbfa;
    --stage: #e9e9e9;
    --ink: #2f2a24;
    --white: #ffffff;
  }
  * { box-sizing: border-box; margin: 0; padding: 0; }
  html, body { width: 1200px; height: 1200px; overflow: hidden; }
  body { background: var(--stage); position: relative; font-family: "Ubuntu", sans-serif; }

  .panel {
    position: absolute; top: 150px; width: 510px; height: 900px;
    background: var(--paper); overflow: hidden;
    box-shadow: 0 6px 24px rgba(0,0,0,.12);
  }
  .panel--front { left: 60px; }
  .panel--back { left: 630px; }

  .wheat-art {
    position: absolute; left: 0;
    background: linear-gradient(160deg, var(--gold-light), var(--gold));
    border-radius: 0 120px 0 0; opacity: .9;
  }
  .panel--front .wheat-art { top: 190px; width: 160px; height: 710px; }
  .panel--back .wheat-art { top: 150px; width: 170px; height: 750px; }

  .stamp-portrait {
    position: absolute; border-radius: 50%;
    background: radial-gradient(circle, #f4ecd9 0%, #e8dcc0 70%);
    border: 3px solid var(--brown);
  }
  .panel--front .stamp-portrait { left: 110px; top: 600px; width: 160px; height: 160px; }
  .panel--back .stamp-portrait { left: 65px; top: 310px; width: 140px; height: 140px; }

  .brand {
    position: absolute; display: flex; align-items: center; gap: 8px;
    font-family: "Oswald", sans-serif; font-weight: 500; color: var(--brown);
    letter-spacing: .5px; white-space: nowrap;
  }
  .brand__dot { width: 20px; height: 20px; border-radius: 50%; background: var(--brown); }
  .panel--front .brand { top: 110px; left: 225px; font-size: 28px; }
  .panel--back .brand { top: 100px; left: 270px; font-size: 24px; }

  .title {
    position: absolute; font-family: "Oswald", sans-serif; font-weight: 700;
    color: var(--brown); text-transform: uppercase; white-space: nowrap; text-align: center;
  }
  .panel--front .title { top: 185px; left: 165px; width: 335px; font-size: 108px; line-height: 1.08; }
  .panel--back .title { top: 150px; left: 200px; width: 305px; font-size: 44px; line-height: 1.2; }

  .claims { position: absolute; top: 540px; left: 320px; display: flex; gap: 22px; }
  .claims__organic { width: 72px; height: 72px; border-radius: 50%; border: 3px solid var(--green); }
  .claims__nongmo { width: 86px; height: 58px; margin-top: 7px; border: 3px solid var(--green); }

  .rule { position: absolute; height: 2px; background: var(--brown); }
  .panel--front .rule { top: 640px; left: 300px; width: 190px; }
  .panel--back .rule { top: 280px; left: 225px; width: 275px; }

  .promise {
    position: absolute; top: 655px; left: 300px; width: 200px;
    font-weight: 700; font-size: 25px; line-height: 1.2; color: var(--brown);
  }

  .range-band {
    position: absolute; top: 790px; left: 0; width: 510px; height: 80px;
    background: var(--gold); display: flex; align-items: center;
    padding-left: 50px;
  }
  .range-band__text { color: var(--white); font-weight: 500; font-size: 14.5px; line-height: 1.4; white-space: nowrap; }
  .range-band__size {
    position: absolute; right: 22px; top: -12px; width: 104px; height: 104px;
    border-radius: 50%; background: var(--brown); border: 4px solid var(--white);
    display: flex; align-items: center; justify-content: center;
    font-family: "Oswald", sans-serif; font-weight: 700; font-size: 34px; color: var(--white);
  }

  .range-list {
    position: absolute; top: 212px; left: 200px; width: 305px; text-align: center;
    font-weight: 500; font-size: 14px; line-height: 1.45; color: var(--brown); white-space: nowrap;
  }

  .story {
    position: absolute; top: 298px; left: 225px; width: 275px;
    font-family: "PT Sans Narrow", sans-serif; font-size: 12px; line-height: 1.42;
    color: var(--ink); text-align: justify;
  }
  .story p + p { margin-top: 10px; }
  .story strong { font-weight: 700; }

  .web {
    position: absolute; top: 852px; right: 22px;
    font-weight: 700; font-size: 16px; color: var(--brown);
  }
</style>
</head>
<body>

<section class="panel panel--front">
  <div class="wheat-art" role="img" aria-label="Golden wheat stalk and leaf illustration"></div>
  <div class="stamp-portrait" role="img" aria-label="Round 'Tovo approves' stamp with a portrait of grandfather Tovo"></div>

  <div class="brand"><span class="brand__dot"></span>TOVO'S GRIST</div>
  <h1 class="title">Tovo's<br>Flour</h1>

  <div class="claims">
    <div class="claims__organic" aria-label="Organic claim badge"></div>
    <div class="claims__nongmo" aria-label="Non GMO claim badge"></div>
  </div>
  <div class="rule"></div>
  <p class="promise">Stone Milled &amp; Family Owned</p>

  <div class="range-band">
    <p class="range-band__text">All Purpose Flour, Pastry Flour,<br>Whole Wheat Flour, Artisan (Bread) Flour</p>
    <div class="range-band__size">1KG</div>
  </div>
</section>

<section class="panel panel--back">
  <div class="wheat-art" role="img" aria-label="Golden wheat stalk and leaf illustration"></div>
  <div class="stamp-portrait" role="img" aria-label="Round 'Tovo approves' stamp with a portrait of grandfather Tovo"></div>

  <div class="brand"><span class="brand__dot"></span>TOVO'S GRIST</div>
  <h2 class="title">Tovo's Flour</h2>
  <p class="range-list">All Purpose Flour, Pastry Flour,<br>Whole Wheat Flour, Artisan (Bread) Flour</p>
  <div class="rule"></div>

  <div class="story">
    <p><strong>Tovo's flour</strong> brings a new kind of flour with nutritional value unmatched by the competition. Our stone milled flour is the first of its kind in the Balkans, and it keeps growing in popularity as more people choose healthy living. Place your order early before each batch sells out, and visit us online to learn more.</p>
    <p><strong>Tovo's flour</strong> is stone ground flour, a method that dates back to prehistoric times and was mastered over centuries before cheaper roller milling took over. We skip the processing steps that harm your food, and bring stone milling back to Macedonia so no toxins reach your flour.</p>
    <p><strong>Tovo's Grist</strong> takes whole grain and produces white and whole wheat flour on modern stone mills. The bran and the nutty germ mix with the endosperm, so your bread keeps its savory taste. Roller mills burn that nutrition away with heat and friction.</p>
    <p><strong>Our Mission</strong> - We bring fresh stone ground flour from organic grain. We make freshness a priority and remove bleaching, chemicals and enriched additives. Try Tovo's flour, the only flour that <strong>Tovo approves</strong>.</p>
  </div>

  <p class="web">tovosgrist.com</p>
</section>

</body>
</html>
```